Criação de Papelaria Profissional para Beleza
" CLÍNICA DE ESTÉTICA COMPLETA, COM ÊNFASE EM ATENDIMENTO PRÊMIUM (salas exclusivas, máquinas próprias, ambiente aconchegante com forte conexão nordestina) Serviços ofertados: Estética corporal, facial, injetáveis e laser) SITE: https://brunelva.com.br/ "

```html
<!DOCTYPE html>
<html lang="pt-BR">
<head>
<meta charset="utf-8">
<title>Brunelva — Envelope</title>
<link rel="stylesheet" href="https://fonts.googleapis.com/css2?family=Cormorant+Garamond:wght@500&family=Montserrat:wght@400;500&display=swap">
<style>
  :root {
    --backdrop: #cd7f78;
    --paper: #f9e8e6;
    --paper-shade: #f2d6d2;
    --rose: #c9716b;
    --rose-soft: #d69891;
    --flap: #d98b84;
  }
  * { margin: 0; padding: 0; box-sizing: border-box; }
  html, body { width: 1200px; height: 1200px; overflow: hidden; }
  body {
    background: var(--backdrop);
    display: flex; flex-direction: column; align-items: center; justify-content: center;
    gap: 60px;
    font-family: "Montserrat", sans-serif;
  }
  .envelope {
    position: relative;
    width: 800px; height: 380px;
    background: var(--paper);
    overflow: hidden;
    box-shadow: 0 12px 30px rgba(120, 50, 45, 0.18);
  }
  .decor-pill {
    position: absolute;
    left: 110px; top: -40px;
    width: 230px; height: 460px;
    border-radius: 115px;
    background: var(--paper-shade);
  }
  .brand {
    position: absolute;
    display: flex; flex-direction: column; align-items: center;
    color: var(--rose);
  }
  .brand-dot {
    width: 30px; height: 30px; border-radius: 50%;
    background: var(--rose);
    margin-bottom: 14px;
  }
  .brand-name {
    font-family: "Cormorant Garamond", serif;
    font-weight: 500;
    letter-spacing: 0.38em;
    margin-right: -0.38em;
    color: var(--rose);
  }
  .brand-tagline {
    font-size: 9px; letter-spacing: 0.45em;
    text-transform: uppercase; color: var(--rose-soft);
    margin-top: 8px;
  }
  .front .brand { left: 450px; top: 120px; }
  .front .brand-name { font-size: 38px; }
  .website {
    position: absolute; left: 450px; top: 262px; width: 290px;
    text-align: center; font-size: 14px; letter-spacing: 0.12em;
    color: var(--rose);
  }
  .back .brand { left: 50%; top: 70px; transform: translateX(-50%); }
  .back .brand-dot { width: 22px; height: 22px; margin-bottom: 10px; }
  .back .brand-name { font-size: 24px; }
  .back .brand-tagline { font-size: 7px; }
  .contacts {
    position: absolute; left: 0; right: 0; top: 190px;
    display: flex; justify-content: center; gap: 18px;
    font-size: 10px; color: var(--rose);
  }
  .contact { display: flex; align-items: center; gap: 6px; }
  .contact-mark { width: 9px; height: 9px; border-radius: 50%; background: var(--rose); }
  .address {
    position: absolute; left: 0; right: 0; top: 218px;
    text-align: center; font-size: 10px; line-height: 1.6; color: var(--rose);
  }
  .flap-edge {
    position: absolute; left: 0; bottom: 0; width: 100%; height: 100px;
  }
</style>
</head>
<body>
  <section class="envelope front" aria-label="Frente do envelope">
    <div class="decor-pill" role="img" aria-label="Forma decorativa suave do símbolo da marca"></div>
    <div class="brand">
      <span class="brand-dot"></span>
      <span class="brand-name">BRUNELVA</span>
      <span class="brand-tagline">Clínica de Estética</span>
    </div>
    <p class="website">brunelva.com.br</p>
  </section>

  <section class="envelope back" aria-label="Verso do envelope">
    <div class="decor-pill" role="img" aria-label="Forma decorativa suave do símbolo da marca"></div>
    <div class="brand">
      <span class="brand-dot"></span>
      <span class="brand-name">BRUNELVA</span>
      <span class="brand-tagline">Clínica de Estética</span>
    </div>
    <div class="contacts">
      <span class="contact">
        <svg width="11" height="11" viewBox="0 0 24 24" aria-hidden="true"><path fill="#c9716b" d="M6.6 10.8a15.1 15.1 0 0 0 6.6 6.6l2.2-2.2a1 1 0 0 1 1-.25 11.4 11.4 0 0 0 3.6.57 1 1 0 0 1 1 1V20a1 1 0 0 1-1 1A17 17 0 0 1 3 4a1 1 0 0 1 1-1h3.5a1 1 0 0 1 1 1c0 1.25.2 2.45.57 3.57a1 1 0 0 1-.25 1z"/></svg>
        (85) 90000-4127
      </span>
      <span class="contact"><span class="contact-mark"></span>@brunelvaestetica</span>
    </div>
    <p class="address">Av. das Acácias, 2.150 - Meireles<br>Fortaleza - CE - Salas 401/402</p>
    <svg class="flap-edge" viewBox="0 0 800 100" preserveAspectRatio="none" aria-hidden="true">
      <path d="M0 100 L0 70 L360 70 Q400 62 440 70 L800 70 L800 100 Z" fill="var(--flap)"/>
    </svg>
  </section>
</body>
</html>
```